Business card for a young woman who performs life enhancement activities with people who have developmental disabilities, what used to be called retardation. She wants to focus on the creative part of her work. She has a degree in art and will engage clients in art projects as well as helping them learn to do things like grocery shop, cook meals, set goals, and live independently.

Target Market(s)

Parents, caregivers, guardians, relatives of people with developmental disabilities, meaning they have not developed in their mental capacities.

Industry/Entity Type

Business

Contact Information for Business Card

Bright Harbor Services, Marisa T. Dunlop, 417 362-8094, marisa@marisadunlop.example, Life enhancement services for people with developmental disabilities. No address.

Font styles to use
Serif

Requirements
Must have
• Marisa wants it to have some indication of the art or creative part of her work with clients. But it must also be businesslike so it appeals to the parents. They have to see her as a professional, but she's compassionate and artsy. She wants just her company name on the front. The other information should be on the back.

```html
<!DOCTYPE html>
<html lang="en">
<head>
<meta charset="utf-8">
<title>Bright Harbor Services – Business Card</title>
<link rel="stylesheet" href="https://fonts.googleapis.com/css2?family=Lora:wght@400;500&display=swap">
<style>
  :root {
    --backdrop: #e9e4dc;
    --card-white: #fbfbfa;
    --card-black: #0c0c0c;
    --ink-dark: #2b2b2b;
    --ink-grey: #8a8a8a;
    --rule: #bdbdbd;
    --accent: #f0902a;
    --paint-yellow: #f2d23a;
    --paint-orange: #f0902a;
    --paint-red: #e8503a;
    --paint-magenta: #c93a9c;
    --band: #b9b9b9;
    --band-ink: #1e1e1e;
    --photo-a: #3a2a24;
    --photo-b: #c99a82;
    --photo-c: #e8d0b4;
    --spectrum: linear-gradient(90deg, var(--paint-yellow), var(--paint-orange), var(--paint-red), var(--paint-magenta));
  }
  * { box-sizing: border-box; margin: 0; padding: 0; }
  html, body {
    width: 1200px; height: 1023px; overflow: hidden;
    background: var(--backdrop);
    font-family: "Lora", Georgia, serif;
  }
  .canvas { position: relative; width: 1200px; height: 1023px; }

  .card {
    position: absolute; width: 700px; height: 400px;
    border-radius: 4px; overflow: hidden;
    box-shadow: 0 10px 28px rgba(0,0,0,0.22);
  }
  .paint-stripe {
    position: absolute; left: 0; right: 0; height: 8px; background: var(--spectrum);
  }

  /* Back side: contact details */
  .card--back { left: 70px; top: 70px; background: var(--card-white); }
  .card--back .paint-stripe { bottom: 0; }
  .card--back .brand {
    position: absolute; left: 50px; top: 0; bottom: 0; width: 270px;
    display: flex; flex-direction: column; justify-content: center; gap: 18px;
  }
  .brand-mark {
    width: 56px; height: 56px; border-radius: 50%; background: var(--accent);
  }
  .brand-name {
    color: var(--accent); font-size: 34px; line-height: 1.15; font-weight: 400;
  }
  .divider {
    position: absolute; left: 350px; top: 70px; bottom: 70px;
    width: 2px; background: linear-gradient(180deg, var(--paint-yellow), var(--paint-orange), var(--paint-red), var(--paint-magenta));
  }
  .contact {
    position: absolute; left: 390px; top: 0; bottom: 0; right: 24px;
    display: flex; flex-direction: column; justify-content: center; gap: 14px;
    color: var(--ink-dark);
  }
  .contact-name { font-size: 24px; letter-spacing: 1px; text-transform: uppercase; margin-bottom: 8px; }
  .contact-line { display: flex; align-items: center; gap: 10px; font-size: 16px; white-space: nowrap; }
  .contact-icon { width: 20px; height: 20px; flex: none; }

  /* Front side: company name */
  .card--front { left: 430px; top: 560px; background: var(--card-black); }
  .card--front .paint-stripe { top: 0; }
  .card--front .brand {
    position: absolute; left: 50px; top: 40px; width: 360px;
    display: flex; flex-direction: column; gap: 16px;
  }
  .card--front .brand-name { font-size: 40px; }
  .tagline-band {
    position: absolute; left: 0; right: 0; top: 232px; height: 38px;
    background: var(--band); color: var(--band-ink);
    font-size: 16px; white-space: nowrap;
    display: flex; align-items: center; padding-left: 50px;
    z-index: 1;
  }
  .photo {
    position: absolute; left: 300px; right: 0; top: 200px; bottom: 0;
    background: linear-gradient(100deg, var(--photo-a) 0%, var(--photo-b) 45%, var(--photo-c) 100%);
  }
</style>
</head>
<body>
<main class="canvas">

  <section class="card card--back" aria-label="Card back">
    <div class="brand">
      <span class="brand-mark"></span>
      <p class="brand-name">Bright Harbor<br>Services</p>
    </div>
    <div class="divider"></div>
    <div class="contact">
      <p class="contact-name">Marisa T. Dunlop</p>
      <p class="contact-line">
        <svg class="contact-icon" viewBox="0 0 20 20" aria-hidden="true">
          <circle cx="10" cy="10" r="10" fill="#f0902a"/>
          <path d="M6.5 5.5c.6-.6 1.4-.5 1.8.1l.9 1.4c.3.5.2 1.1-.2 1.4l-.6.5c.5 1.1 1.4 2 2.5 2.5l.5-.6c.4-.4 1-.5 1.4-.2l1.4.9c.6.4.7 1.2.1 1.8l-.6.6c-.8.8-2.6.4-4.5-1.5S5.1 6.9 5.9 6.1z" fill="#fff"/>
        </svg>
        417 362-8094
      </p>
      <p class="contact-line">
        <svg class="contact-icon" viewBox="0 0 20 20" aria-hidden="true">
          <circle cx="10" cy="10" r="10" fill="#f0902a"/>
          <rect x="5" y="6.5" width="10" height="7" rx="1" fill="#fff"/>
          <path d="M5.4 7l4.6 3.6L14.6 7" fill="none" stroke="#f0902a" stroke-width="1"/>
        </svg>
        marisa@marisadunlop.example
      </p>
    </div>
    <div class="paint-stripe"></div>
  </section>

  <section class="card card--front" aria-label="Card front">
    <div class="paint-stripe"></div>
    <div class="photo" role="img" aria-label="Photograph of two smiling women posing together"></div>
    <div class="brand">
      <span class="brand-mark"></span>
      <p class="brand-name">Bright Harbor<br>Services</p>
    </div>
    <p class="tagline-band">Life enhancement services for people with developmental disabilities</p>
  </section>

</main>
</body>
</html>
```